Power Point Template Kalmora sustainability consulting

Please note:
We are not looking for new design proposals anymore since we've already received templetes from two designers that we really like. We are currently discussing possible changes with them and will make a final decision soon. Thank you very much.

(find english description below)
We are a small German start-up that offers sustainability consulting. For presentations of results, our company presentation, proposals, lectures, etc., we need a PowerPoint template that matches our logo. We come from classic management consulting / strategy consulting and also deal with facts and figures in sustainability consulting. Therefore, the template should not be too fancy and should not only consist of photos. But it shouldn't be a completely sober template either. Our logo with the green leaves for sustainability (three leaves for KALmora) and the white bar chart (with the dynamic swing upwards) reflects our attitude well, where we see ourselves on the range from playful to sober and classic to modern.

It might be nice for the template to include the shape of one of the leaves (from the logo). Also, the logo should appear in a corner of each slide. The colors from the logo (see appendix) should be partially reflected in the presentation. We can also imagine a gold-brown tone (see website www.kalmora-consulting.example) or a coral tone as a contrast. (Attention - the website is not final yet).

For a first suggestion, it is sufficient to suggest three to four slides (cover sheet, chapter/separation slide, text slide, data slide). We will then mark drafts that we like. In total, we would then need about 6-10 more slide templates, e.g. about us, team, slide for a statement, 2-3 data charts (pie, bar, column), top 3 - 5 list, timeline, contact (more slides are welcome ).

We are a small German start-up offering sustainability consulting. We need a power point template for result presentations, our company presentation, proposals, lectures etc. The template should be aligned with our logo. Our background lies in classic management consulting / strategy consulting and we also deal with facts and figures in sustainability consulting. Therefore, the template should not be too playful and not only consist of photos. But it should also not be a completely clear template. Our logo with the green leaves for sustainability (three leaves for KALmora) and the white bar chart (with the dynamic upward swing) reflects our attitude well, where we see ourselves on the range from playful to down-to-earth and classic to modern .

For the template, it might be nice to incorporate the shape of one of the leaves (from the logo). Also, the logo should show up in one corner on each slide. Some of the colors from the logo (see attachment) should be reflected in the presentation. We could also think of a gold-brown tone (see website www.kalmora-consulting.example) or a coral tone for contrast. (Attention - the website is not final yet).

For a first proposal it is quite sufficient to suggest us three to four slides (cover page, chapter/separation slide, text slide, data slide). We will then mark the drafts that we like. In total we would need about 6-10 more slide templates, eg About us, Team, slide for a statement, 2-3 data charts (pie, bar, column), Top 3 - 5 List, Timeline, Contact (more slides are welcome).

Target Market(s)

Corporations, large companies and SMEs

Industry/Entity Type

Unternehmensberatung, Nachhaltigkeitsberatung

Font styles to use
Sans Serif
Other font styles liked:
• Calibri

Colors
00AB8E
00BBA5
67D7C9
C6EFE9
E9F9F6

Requirements
Must have
• see description (e.g. the colors of our logo)
Nice to have
• see description (e.g. elements of the logo included)
Should not have
• see description

```html
<!DOCTYPE html>
<html lang="en">
<head>
<meta charset="utf-8">
<title>Kalmora – Presentation Template</title>
<link rel="stylesheet" href="https://fonts.googleapis.com/css2?family=Arimo:wght@400;700&display=swap">
<style>
:root{
  --forest:#34491f;
  --green:#3f7412;
  --green-light:#6a9a35;
  --beige:#d8caa6;
  --beige-dark:#7d7257;
  --white:#ffffff;
  --grey:#6b6b6b;
  --bar-grey:#8a8a8a;
}
*{margin:0;padding:0;box-sizing:border-box}
html,body{width:1200px;height:4216px;overflow:hidden;background:var(--forest)}
body{font-family:"Arimo",Arial,sans-serif}
.board{position:absolute;left:0;top:0;width:733px;height:2576px;transform:scale(1.6371);transform-origin:0 0;background:var(--forest)}
.slide{position:absolute;left:36px;width:661px;height:371px;background:var(--white);overflow:hidden}
.abs{position:absolute}
.brand{position:absolute;display:flex;align-items:center;gap:5px;color:var(--grey);font-weight:400;letter-spacing:.2px}
.brand .dot{width:11px;height:11px;border-radius:50%;background:var(--green)}
.url-strip{position:absolute;left:604px;top:23px;width:34px;height:326px;background:var(--beige);display:flex;align-items:flex-end;justify-content:center;padding-bottom:22px}
.url-strip span{writing-mode:vertical-rl;transform:rotate(180deg);font-weight:700;font-size:11px;color:var(--beige-dark);letter-spacing:.2px}
.photo{position:absolute}
.heading{font-weight:700;text-transform:uppercase;letter-spacing:.6px}
.title-box{position:absolute;left:178px;top:65px;width:241px;height:47px;background:var(--green);color:var(--white);font-size:19px;display:flex;align-items:center;padding-left:23px}
.beige{position:absolute;background:var(--beige)}
.page-badge{position:absolute;display:flex;flex-direction:column;align-items:center;justify-content:center;font-weight:700}
.page-badge small{font-size:6px;letter-spacing:.4px}
.page-badge b{font-size:17px;line-height:1}
.objective{position:absolute;width:190px}
.objective .tick{position:absolute;left:-46px;top:-4px;width:34px;height:24px}
.objective h3{font-size:11.5px;color:var(--green);font-weight:700;letter-spacing:.4px;margin-bottom:3px}
.objective p{font-size:8.2px;line-height:1.25;color:var(--white);font-weight:700;width:115px}
</style>
</head>
<body>
<div class="board">

  <!-- Cover -->
  <section class="slide" style="top:34px">
    <div class="photo" role="img" aria-label="Sunlit park trees in front of city high-rises with green lawn" style="left:42px;top:23px;width:563px;height:326px;background:linear-gradient(90deg,#fff 0%,rgba(255,255,255,.9) 25%,rgba(255,255,255,0) 55%),linear-gradient(180deg,#d9dcd4 0%,#8e9a6c 30%,#4d6a24 55%,#3c5a1c 75%,#8cb23a 100%)"></div>
    <div class="url-strip"><span>www.kalmora-consulting.example</span></div>
    <div class="brand" style="left:44px;top:76px;font-size:24px"><span class="dot"></span>Kalmora</div>
    <div class="abs" style="left:0;top:154px;width:422px;height:128px;background:rgba(63,116,18,.92)"></div>
    <div class="abs heading" style="left:41px;top:178px;color:var(--white);font-size:12px">Kalmora Consulting</div>
    <div class="abs heading" style="left:40px;top:195px;color:var(--beige);font-size:29px;line-height:1.12;letter-spacing:1px">Business<br>Presentation</div>
    <div class="abs" style="left:0;top:282px;width:422px;height:32px;background:var(--beige)"></div>
    <div class="abs heading" style="left:41px;top:292px;color:var(--beige-dark);font-size:12px">Kalmora Consulting</div>
  </section>

  <!-- Text slide -->
  <section class="slide" style="top:457px">
    <div class="brand" style="left:42px;top:35px;font-size:16px"><span class="dot"></span>Kalmora</div>
    <div class="photo" role="img" aria-label="Sun rays through a forest canopy above a dark railing" style="left:313px;top:23px;width:291px;height:326px;background:radial-gradient(circle at 65% 25%,#e6dcb4 0%,#8f8a52 18%,#3b4a1e 45%,#1b2410 80%)"></div>
    <div class="url-strip"><span>www.kalmora-consulting.example</span></div>
    <div class="abs" style="left:30px;top:122px;width:333px;height:170px;background:var(--white);box-shadow:0 1px 6px rgba(0,0,0,.3)"></div>
    <div class="abs heading" style="left:30px;top:79px;width:333px;height:43px;background:var(--beige);color:var(--green);font-size:17px;padding:12px 0 0 24px">Text Slide</div>
    <p class="abs" style="left:54px;top:140px;width:285px;font-size:9.6px;line-height:1.2;color:var(--green)">Quisque in augue. Donec aliquam magna nonummy enim. Proin blandit imperdiet sem. Donec malesuada, urna sit amet varius aliquam, nibh tortor laoreet turpis, eget sodales felis nibh ac sapien. Fusce eget augue. Integer sed risus. Aenean mollis. Donec facilisis egestas quam. Duis bibendum augue id mauris. Sed laoreet, tortor vel cursus fringilla, turpis elit vestibulum arcu, eu varius dolor leo in nulla. In sem ipsum, faucibus quis, varius tristique, porta eget, lorem. Curabitur hendrerit diam et mauris. Etiam porta nunc euismod dui. Maecenas a lectus. In hac</p>
    <div class="page-badge" style="left:40px;top:329px;width:38px;height:42px;background:var(--beige);color:var(--white)"><small>PAGE</small><b>5</b></div>
  </section>

  <!-- Objectives -->
  <section class="slide" style="top:880px">
    <div class="beige" style="left:157px;top:23px;width:472px;height:90px"></div>
    <div class="beige" style="left:19px;top:112px;width:610px;height:237px"></div>
    <div class="brand" style="left:38px;top:55px;font-size:16px"><span class="dot"></span>Kalmora</div>
    <div class="title-box heading">Our Objectives</div>
    <div class="objective" style="left:178px;top:163px">
      <svg class="tick" viewBox="0 0 34 24"><circle cx="17" cy="12" r="11" fill="#3f7412"/><path d="M11 12l4 4 8-8" fill="none" stroke="#fff" stroke-width="2.4" stroke-linecap="round" stroke-linejoin="round"/></svg>
      <h3>Our Objectives</h3><p>90% Quisque in augue. Donec aliquam magna nonummy enim. Proin blandit imperdiet sem.</p>
    </div>
    <div class="objective" style="left:395px;top:163px">
      <svg class="tick" viewBox="0 0 34 24"><circle cx="17" cy="12" r="11" fill="#3f7412"/><path d="M11 12l4 4 8-8" fill="none" stroke="#fff" stroke-width="2.4" stroke-linecap="round" stroke-linejoin="round"/></svg>
      <h3>Our Objectives</h3><p>90% Quisque in augue. Donec aliquam magna nonummy enim. Proin blandit imperdiet sem.</p>
    </div>
    <div class="objective" style="left:178px;top:246px">
      <svg class="tick" viewBox="0 0 34 24"><circle cx="17" cy="12" r="11" fill="#3f7412"/><path d="M11 12l4 4 8-8" fill="none" stroke="#fff" stroke-width="2.4" stroke-linecap="round" stroke-linejoin="round"/></svg>
      <h3>Our Objectives</h3><p>90% Quisque in augue. Donec aliquam magna nonummy enim. Proin blandit imperdiet sem.</p>
    </div>
    <div class="objective" style="left:395px;top:246px">
      <svg class="tick" viewBox="0 0 34 24"><circle cx="17" cy="12" r="11" fill="#3f7412"/><path d="M11 12l4 4 8-8" fill="none" stroke="#fff" stroke-width="2.4" stroke-linecap="round" stroke-linejoin="round"/></svg>
      <h3>Our Objectives</h3><p>90% Quisque in augue. Donec aliquam magna nonummy enim. Proin blandit imperdiet sem.</p>
    </div>
  </section>

  <!-- Chapter slide -->
  <section class="slide" style="top:1303px">
    <div class="brand" style="left:38px;top:55px;font-size:16px"><span class="dot"></span>Kalmora</div>
    <div class="photo" role="img" aria-label="Misty green mountain valley with a small village" style="left:167px;top:23px;width:437px;height:326px;background:linear-gradient(180deg,#c9ccc3 0%,#9aa293 28%,#4f6a3a 50%,#2f4a1e 75%,#3d5a22 100%)"></div>
    <div class="url-strip"><span>www.kalmora-consulting.example</span></div>
    <div class="beige" style="left:19px;top:149px;width:260px;height:160px"></div>
    <div class="abs heading" style="left:45px;top:172px;width:220px;color:var(--beige-dark);font-size:14px;line-height:1.15">Chapter/Separation<br>Slide</div>
    <p class="abs" style="left:45px;top:222px;width:205px;font-size:8.4px;font-weight:700;line-height:1.22;color:var(--green)">chapter/separation slide Quisque in augue. Donec aliquam magna nonummy enim. Proin blandit imperdiet sem. Donec malesuada, urna sit amet varius</p>
  </section>

  <!-- Data slide -->
  <section class="slide" style="top:1726px">
    <div class="beige" style="left:157px;top:23px;width:472px;height:90px"></div>
    <div class="beige" style="left:19px;top:112px;width:610px;height:237px"></div>
    <div class="brand" style="left:38px;top:55px;font-size:16px"><span class="dot"></span>Kalmora</div>
    <div class="title-box heading">Data Analyze</div>
    <svg class="abs" style="left:80px;top:145px" width="230" height="165" viewBox="0 0 230 165">
      <g fill="none" stroke="#8a8a8a" stroke-width="2"><path d="M4 8V156H224"/></g>
      <rect x="17" y="136" width="13" height="19" fill="#8a8a8a"/>
      <rect x="42" y="118" width="12" height="37" fill="#8a8a8a"/>
      <rect x="67" y="95" width="13" height="60" fill="#3f7412"/>
      <rect x="92" y="27" width="13" height="128" fill="#fff"/>
      <rect x="117" y="82" width="12" height="73" fill="#8a8a8a"/>
      <rect x="141" y="40" width="13" height="115" fill="#fff"/>
      <rect x="166" y="82" width="13" height="73" fill="#8a8a8a"/>
      <rect x="191" y="82" width="13" height="73" fill="#8a8a8a"/>
      <text x="98" y="20" font-size="7" font-weight="700" fill="#3f7412" text-anchor="middle" font-family="Arimo, Arial, sans-serif">95%</text>
      <text x="147" y="33" font-size="7" font-weight="700" fill="#3f7412" text-anchor="middle" font-family="Arimo, Arial, sans-serif">90%</text>
    </svg>
    <div class="abs" style="left:354px;top:140px;font-size:26px;font-weight:700;color:var(--green)">95%</div>
    <p class="abs" style="left:354px;top:175px;width:115px;font-size:8.2px;font-weight:700;line-height:1.22;color:var(--white)">90% Quisque in augue. Donec aliquam magna nonummy enim. Proin blandit imperdiet sem.</p>
    <div class="abs" style="left:354px;top:232px;font-size:26px;font-weight:700;color:var(--green-light)">90%</div>
    <p class="abs" style="left:354px;top:268px;width:115px;font-size:8.2px;font-weight:700;line-height:1.22;color:var(--white)">90% Quisque in augue. Donec aliquam magna nonummy enim. Proin blandit imperdiet sem.</p>
    <svg class="abs" style="left:514px;top:141px" width="72" height="170" viewBox="0 0 72 170">
      <circle cx="36" cy="36" r="28" fill="none" stroke="#3f7412" stroke-width="11" stroke-dasharray="165 11" transform="rotate(-80 36 36)"/>
      <circle cx="36" cy="132" r="28" fill="none" stroke="#6a9a35" stroke-width="11" stroke-dasharray="168 8" transform="rotate(-82 36 132)"/>
    </svg>
  </section>

  <!-- Two-column slide -->
  <section class="slide" style="top:2149px">
    <div class="beige" style="left:32px;top:23px;width:172px;height:326px"></div>
    <div class="photo" role="img" aria-label="Dense dark green foliage" style="left:204px;top:23px;width:400px;height:326px;background:radial-gradient(circle at 30% 30%,#3f6a22 0%,#24401a 60%,#1a3012 100%)"></div>
    <div class="url-strip"><span>www.kalmora-consulting.example</span></div>
    <div class="abs" style="left:56px;top:23px;width:124px;height:57px;background:var(--white)"></div>
    <div class="brand" style="left:68px;top:42px;font-size:16px"><span class="dot"></span>Kalmora</div>
    <div class="abs heading" style="left:57px;top:102px;color:var(--green);font-size:15px;line-height:1.05">Some Title<br>Here</div>
    <div class="photo" role="img" aria-label="Hands holding a young green seedling in soil" style="left:54px;top:141px;width:126px;height:84px;background:linear-gradient(135deg,#9cc15a 0%,#4e7d28 55%,#2c4a16 100%)"></div>
    <p class="abs" style="left:54px;top:233px;width:126px;font-size:6.4px;font-weight:700;line-height:1.22;color:var(--beige-dark)">chapter/separation slide Quisque in augue. Donec aliquam magna nonummy enim. Proin blandit imperdiet sem. Donec malesuada, urna sit amet varius</p>
    <div class="page-badge" style="left:56px;top:317px;width:38px;height:32px;background:var(--white);color:var(--beige-dark)"><small>PAGE</small><b style="color:#a8944f">5</b></div>
    <div class="abs heading" style="left:244px;top:77px;color:var(--beige);font-size:12px;line-height:1.1">Curabitur<br>Libero</div>
    <p class="abs" style="left:244px;top:107px;width:150px;font-size:9.4px;line-height:1.22;color:var(--white)">Quisque in augue. Donec aliquam magna nonummy enim. Proin blandit imperdiet sem. Donec malesuada, urna sit amet varius aliquam, nibh tortor laoreet turpis, eget sodales felis nibh ac sapien. Fusce eget augue. Integer sed risus. Aenean mollis. Donec facilisis egestas quam. Duis bibendum augue id mauris. Sed laoreet, tortor vel cursus fringilla, turpis elit vestibulum arcu, eu varius dolor leo in nulla. In sem</p>
    <div class="abs heading" style="left:430px;top:77px;color:var(--beige);font-size:12px;line-height:1.1">Curabitur<br>Libero</div>
    <p class="abs" style="left:430px;top:107px;width:150px;font-size:9.4px;line-height:1.22;color:var(--white)">Quisque in augue. Donec aliquam magna nonummy enim. Proin blandit imperdiet sem. Donec malesuada, urna sit amet varius aliquam, nibh tortor laoreet turpis, eget sodales felis nibh ac sapien. Fusce eget augue. Integer sed risus. Aenean mollis. Donec facilisis egestas quam. Duis bibendum augue id mauris. Sed laoreet, tortor vel cursus fringilla, turpis elit vestibulum arcu, eu varius dolor leo in nulla. In sem</p>
  </section>

</div>
</body>
</html>
```